Olive Oil Label Needs Graphic Designs

We need two sister label designs for 500ml bottles for our new brand "Casa Lumbre". Casa Lumbre is a high-end olive oil from Baeza, Spain which will be sold in the US. The oil will be produced from both Arbequina olives and Picual olives. Therefore, envisioning the same design just a different color scheme for the different labels.
The label should have the following characteristics; clean and simple, stand-out from mainstream labels, be eye-catching, give perception of high-end / high-quality.
Our current thinking of what we want (but please let your creative juices flow); lighter background, to be more eye catching, graphics of and olive, a olive branch or olive tree.
Text which should appear on the label are (not necessarily in this order);
Casa Lumbre
Extra Virgin Olive Oil
Family Reserve
Arbequina (One design)
Picual (Second design)
The label should be about 3 inches wide and 5.5 inches in height.

```html
<!DOCTYPE html>
<html lang="en">
<head>
<meta charset="utf-8">
<title>Casa Lumbre – Extra Virgin Olive Oil Labels</title>
<link rel="stylesheet" href="https://fonts.googleapis.com/css2?family=Dancing+Script:wght@500&family=Arimo:wght@400;700&display=swap">
<style>
  :root {
    --canvas: #e9e9ea;
    --label-bg: #ffffff;
    --olive-dark: #4b5a1c;
    --olive: #5f6c1f;
    --olive-text: #6f7b24;
    --orange: #f7941d;
    --seal-dark: #1f4a22;
    --seal-ring: #f4f0df;
    --splash-a: #f3efb3;
    --splash-b: #d7cf53;
    --tree-leaf: #7a9a3a;
    --tree-trunk: #5a4a1f;
    --footer-text: #6b6b6b;
  }
  * { margin: 0; padding: 0; box-sizing: border-box; }
  html, body { width: 1200px; height: 1000px; overflow: hidden; }
  body {
    background: var(--canvas);
    font-family: "Arimo", Arial, sans-serif;
    display: flex;
    justify-content: center;
    align-items: center;
    gap: 60px;
  }
  .label {
    position: relative;
    width: 420px;
    height: 880px;
    background: var(--label-bg);
    box-shadow: 0 2px 10px rgba(0,0,0,0.12);
    overflow: hidden;
  }
  .label--arbequina { --accent: var(--olive); --title: var(--olive-text); }
  .label--picual { --accent: var(--orange); --title: var(--orange); }

  .oil-splash {
    position: absolute;
    top: 0; left: 0;
    width: 100%;
    height: 270px;
    background:
      radial-gradient(ellipse at 75% 10%, var(--splash-b) 0%, rgba(215,207,83,0.35) 35%, transparent 65%),
      radial-gradient(ellipse at 20% 0%, var(--splash-a) 0%, transparent 60%);
  }
  .brand {
    position: absolute;
    top: 88px;
    left: 50%;
    transform: translateX(-50%);
    background: var(--olive-dark);
    color: #fff;
    font-weight: 700;
    font-size: 24px;
    padding: 9px 22px;
    border-radius: 8px;
    white-space: nowrap;
  }
  .olive-tree {
    position: absolute;
    top: 230px;
    left: 50%;
    transform: translateX(-50%);
    width: 230px;
    height: 140px;
    border-radius: 50% 50% 40% 40%;
    background: radial-gradient(ellipse at 50% 40%, var(--tree-leaf) 0%, #9bb65a 55%, rgba(155,182,90,0.2) 80%, transparent 100%);
  }
  .title {
    position: absolute;
    left: 0; right: 0;
    text-align: center;
    font-family: "Dancing Script", cursive;
    font-weight: 500;
    color: var(--title);
    line-height: 1;
  }
  .title--small { top: 415px; font-size: 62px; letter-spacing: 1px; }
  .title--large { top: 490px; font-size: 100px; letter-spacing: 2px; }
  .variety-band {
    position: absolute;
    top: 632px;
    left: 0;
    width: 100%;
    height: 38px;
    background: var(--accent);
  }
  .variety-seal {
    position: absolute;
    top: 594px;
    left: 272px;
    width: 116px;
    height: 116px;
  }
  .footer {
    position: absolute;
    bottom: 22px;
    left: 36px;
    right: 36px;
    display: flex;
    justify-content: space-between;
    font-size: 17px;
    color: var(--footer-text);
  }
</style>
</head>
<body>

  <section class="label label--arbequina">
    <div class="oil-splash" role="img" aria-label="Splash of golden olive oil"></div>
    <div class="brand">Casa Lumbre</div>
    <div class="olive-tree" role="img" aria-label="Olive tree illustration"></div>
    <h2 class="title title--small">Extra Virgin</h2>
    <h1 class="title title--large">Olive Oil</h1>
    <div class="variety-band"></div>
    <svg class="variety-seal" viewBox="0 0 116 116" aria-label="Arbequina Olives seal">
      <defs>
        <path id="arc-arbequina" d="M 18 58 A 40 40 0 0 1 98 58"/>
      </defs>
      <circle cx="58" cy="58" r="56" fill="#ffffff"/>
      <circle cx="58" cy="58" r="52" fill="var(--seal-dark)"/>
      <circle cx="58" cy="58" r="30" fill="#7c9a3a" role="img" aria-label="Olive illustration"/>
      <text font-family="Arimo, Arial, sans-serif" font-size="11" font-weight="700" fill="var(--seal-ring)" letter-spacing="1">
        <textPath href="#arc-arbequina" startOffset="50%" text-anchor="middle">ARBEQUINA OLIVES</textPath>
      </text>
    </svg>
    <div class="footer"><span>Family Reserve</span><span>500ml</span></div>
  </section>

  <section class="label label--picual">
    <div class="oil-splash" role="img" aria-label="Splash of golden olive oil"></div>
    <div class="brand">Casa Lumbre</div>
    <div class="olive-tree" role="img" aria-label="Olive tree illustration"></div>
    <h2 class="title title--small">Extra Virgin</h2>
    <h1 class="title title--large">Olive Oil</h1>
    <div class="variety-band"></div>
    <svg class="variety-seal" viewBox="0 0 116 116" aria-label="Picual Olives seal">
      <defs>
        <path id="arc-picual" d="M 18 58 A 40 40 0 0 1 98 58"/>
      </defs>
      <circle cx="58" cy="58" r="56" fill="#ffffff"/>
      <circle cx="58" cy="58" r="52" fill="var(--seal-dark)"/>
      <circle cx="58" cy="58" r="30" fill="#7c9a3a" role="img" aria-label="Olive illustration"/>
      <text font-family="Arimo, Arial, sans-serif" font-size="11" font-weight="700" fill="var(--seal-ring)" letter-spacing="1">
        <textPath href="#arc-picual" startOffset="50%" text-anchor="middle">PICUAL OLIVES</textPath>
      </text>
    </svg>
    <div class="footer"><span>Family Reserve</span><span>500ml</span></div>
  </section>

</body>
</html>
```